I need a business card for myself, being a proprietor of a funeral parlor based in Manila. I'd like the card to have either of the following:
White Font on Black Background
or
Black Font on White Background
No logo is needed however I will appreciate any efforts to show a symbol of eternal happiness, aptly designed with above mentioned colors in mind.
Company name, address and contact on the lower right corner.
Logo or symbol anywhere.
Quillstone Funeral Services
+639174826351
darvik4521@pelmora.com
corner of Brisco Avenue and Velhurst Street
Makati City, Philippines
Thank you.
Update: Please include a small dove in your design. You are free to choose where you would like it on the card.

```html
<!DOCTYPE html>
<html lang="en">
<head>
<meta charset="UTF-8">
<title>Quillstone Funeral Services – Business Card</title>
<link rel="stylesheet" href="https://fonts.googleapis.com/css2?family=Roboto+Condensed:wght@400&family=Roboto:wght@400&display=swap">
<style>
  :root {
    --page-bg: #e9e7e3;
    --card-black: #1c1c1c;
    --ink-white: #ffffff;
    --accent-green: #1f9a3a;
    --dove-light: #f4f4f2;
    --dove-shade: #c9c9c6;
  }
  * { margin: 0; padding: 0; box-sizing: border-box; }
  html, body {
    width: 1200px;
    height: 900px;
    overflow: hidden;
    background: var(--page-bg);
  }
  .canvas {
    position: relative;
    width: 1200px;
    height: 900px;
  }
  .business-card {
    position: absolute;
    left: 100px;
    top: 164px;
    width: 1000px;
    height: 572px;
    background: var(--card-black);
    border-radius: 34px;
    overflow: hidden;
    color: var(--ink-white);
  }
  .dove-artwork {
    position: absolute;
    left: 390px;
    top: 40px;
    width: 330px;
    height: 200px;
    border-radius: 50% 50% 40% 40% / 60% 60% 40% 40%;
    background: radial-gradient(ellipse at 45% 45%, var(--dove-light) 0%, var(--dove-light) 45%, var(--dove-shade) 80%, rgba(201,201,198,0) 100%);
  }
  .name-row {
    position: absolute;
    left: 40px;
    right: 50px;
    top: 236px;
    display: flex;
    align-items: flex-end;
  }
  .accent-rule {
    flex: 1;
    height: 3px;
    background: var(--accent-green);
    margin-bottom: 8px;
  }
  .company-name {
    font-family: "Roboto Condensed", "Arial Narrow", sans-serif;
    font-size: 46px;
    font-weight: 400;
    line-height: 1;
    white-space: nowrap;
    letter-spacing: -0.5px;
  }
  .contact-details {
    position: absolute;
    right: 50px;
    top: 306px;
    text-align: right;
    font-family: "Roboto", Arial, sans-serif;
    line-height: 1.25;
  }
  .contact-phone,
  .contact-email {
    font-size: 27px;
    letter-spacing: 2px;
  }
  .contact-street {
    font-family: "Roboto Condensed", "Arial Narrow", sans-serif;
    font-size: 27px;
  }
  .contact-city {
    font-size: 34px;
    letter-spacing: 2px;
  }
</style>
</head>
<body>
  <main class="canvas">
    <section class="business-card">
      <div class="dove-artwork" role="img" aria-label="White dove in flight with wings raised"></div>

      <div class="name-row">
        <div class="accent-rule"></div>
        <h1 class="company-name">Quillstone Funeral Services</h1>
      </div>

      <address class="contact-details" style="font-style: normal;">
        <p class="contact-phone">Phone: +639174826351</p>
        <p class="contact-email">Email: darvik4521@pelmora.com</p>
        <p class="contact-street">Corner of Brisco Avenue and Velhurst Street</p>
        <p class="contact-city">Makati City, Philippines</p>
      </address>
    </section>
  </main>
</body>
</html>
```